Corvane Care Group Presentation Folder, for Cancer Awareness, VERY COLORFUL AND MODERN

Presentation Folder I know pretty much what i want so it should be very eazy , I have included files from folders I use now rebrand them to my new company they will be fine, no sense re creating the wheel
Full Bleed Size
20.87" x 16.68"
53 x 42.4 cm
6260 x 5004 pixels
Document Trim Size
20.75" x 16.56"
52.7 x 42.1 cm
6225 x 4969 pixels
Updates

Low design quality

Industry/Entity Type

Medical

Font styles to use
Serif

Colors

Designer to choose colors to be used in the design.

Requirements
Must have
• really I am not looking for some one to redesign, we like our folder front page and would like to see new word information added., there are two folder front pages to choose from
• So Keep the original front page and redesign the back page and the pockets
• Can Make your Design off of one of the ones I already uploaded
Nice to have
• Keep the same color schemes, Keep the original front page and redesign the back page and the pockets
Should not have
• DO not recreate the front covers, use what I gave you and just rebrand

```html
<!DOCTYPE html>
<html lang="en">
<head>
<meta charset="utf-8">
<title>Corvane Care Group – Presentation Folder Options</title>
<link href="https://fonts.googleapis.com/css2?family=Open+Sans:wght@400;600;700&family=Raleway:wght@400;500;600;700&display=swap" rel="stylesheet">
<style>
  :root{
    --paper:#ffffff;
    --dieline:#e8787f;
    --fold:#8fd08f;
    --safe:#8fd3ee;
    --pink:#f2909c;
    --navy:#0f1f48;
    --lime:#8cc63f;
    --slate:#6b6d70;
    --ink:#1d1d2b;
    --grey-text:#555a60;
    --strip:#cfd0d2;
    --lavender:#b9bddf;
    --sage:#dfeccd;
  }
  *{margin:0;padding:0;box-sizing:border-box}
  html,body{width:720px;height:1200px;overflow:hidden;background:var(--paper)}
  body{position:relative;font-family:"Open Sans",sans-serif;color:var(--ink)}

  .folder{position:absolute;left:36px;width:652px;height:518px}
  .folder--navy{top:42px}
  .folder--lime{top:640px}

  .dieline{position:absolute;inset:0;width:652px;height:518px;overflow:visible}

  .panel-frame{position:absolute;border:1px solid var(--safe)}
  .cover-left{left:36px;top:10px;width:278px;height:356px}
  .cover-right{left:334px;top:10px;width:282px;height:356px}

  .corner-wash{position:absolute;left:26px;top:4px;width:170px;height:150px;
    background:radial-gradient(circle at 65% 25%,var(--lavender) 0,rgba(185,189,223,.45) 30%,rgba(223,236,205,.35) 55%,rgba(255,255,255,0) 75%)}

  .photo{position:absolute;box-shadow:2px 3px 5px rgba(0,0,0,.25)}
  .photo--beach{left:46px;top:90px;width:246px;height:148px;transform:rotate(-3deg);
    background:linear-gradient(180deg,#2f8fe0 0%,#7cc3f0 45%,#e9e3d2 62%,#d8cdb4 100%)}
  .photo--table{left:356px;top:124px;width:250px;height:160px;transform:rotate(-3deg);
    background:linear-gradient(160deg,#f3efe8 0%,#d9c8b0 40%,#8fa7b4 70%,#c9b79c 100%)}

  .ribbon{position:absolute;width:22px;height:46px;transform:rotate(25deg);
    background:linear-gradient(90deg,#d77ab5 0%,#8a9be0 60%,#6fc3e6 100%);border-radius:11px 11px 4px 4px}
  .ribbon--left{left:268px;top:36px}
  .ribbon--right{left:578px;top:100px}

  .cover-copy{position:absolute;left:58px;top:272px;width:250px;font-size:6.4px;line-height:1.35}
  .cover-copy b{font-weight:700}
  .cover-copy .closing{margin-top:7px;font-weight:700;font-size:6.4px}

  .title-band{position:absolute;left:335px;top:25px;width:280px;height:23px;background:var(--pink);
    color:#fff;font-family:"Raleway",sans-serif;font-weight:600;font-size:14px;letter-spacing:1px;
    display:flex;align-items:center;justify-content:center}
  .lead{position:absolute;left:335px;top:55px;width:280px;text-align:center;font-family:"Raleway",sans-serif;font-size:8px;color:var(--ink)}
  .sublead{position:absolute;left:355px;top:68px;width:240px;text-align:center;font-family:"Raleway",sans-serif;font-size:6.3px;line-height:1.3;color:var(--grey-text)}

  .tagline-band{position:absolute;left:335px;top:316px;width:280px;height:22px;background:var(--slate);
    color:#fff;font-family:"Raleway",sans-serif;font-size:9.5px;letter-spacing:.3px;
    display:flex;align-items:center;padding-left:50px}
  .badge{position:absolute;left:364px;top:327px;width:26px;height:26px;border-radius:50%;
    background:#fff;border:2px solid var(--navy)}

  .pocket{position:absolute;top:376px;height:142px;overflow:hidden}
  .pocket--left{left:24px;width:300px;border-radius:0 0 0 12px}
  .pocket--right{left:328px;width:298px;border-radius:0 0 12px 0}
  .pocket-strip{position:absolute;top:0;bottom:0;width:18px;background:var(--strip)}
  .pocket--left .pocket-strip{left:0}
  .pocket--right .pocket-strip{right:0}
  .pocket-wash{position:absolute;left:18px;bottom:0;width:120px;height:130px;
    background:radial-gradient(circle at 20% 80%,rgba(185,189,223,.7) 0,rgba(223,236,205,.45) 45%,rgba(255,255,255,0) 72%)}

  .flipped{position:absolute;transform:rotate(180deg)}
  .brand-block{left:100px;top:16px;width:180px;text-align:center}
  .brand-name{font-family:"Raleway",sans-serif;font-weight:700;font-size:13px;color:var(--navy)}
  .brand-note{font-size:4.6px;color:var(--grey-text);margin-top:2px}
  .brand-mark{left:150px;top:58px;display:flex;align-items:center;gap:5px}
  .brand-mark .dot{width:22px;height:22px;border-radius:50%;border:2px solid var(--navy)}
  .brand-mark span{font-family:"Raleway",sans-serif;font-weight:700;font-size:8px;color:var(--navy)}

  .card-slits{position:absolute;left:0;top:0;width:300px;height:142px}

  .pocket-fill{position:absolute;left:0;top:0;right:18px;bottom:0;border-radius:0 0 0 18px}
  .folder--navy .pocket-fill{background:var(--navy)}
  .folder--lime .pocket-fill{background:var(--lime)}
  .pocket-frame{position:absolute;left:14px;top:10px;width:258px;height:124px;border:1px solid var(--safe);border-radius:0 0 0 14px}
  .pocket-copy{left:22px;top:26px;width:244px}
  .pocket-copy p{font-size:5.4px;line-height:1.45}
  .pocket-copy h3{margin-top:6px;font-family:"Raleway",sans-serif;font-weight:700;font-size:8.6px;line-height:1.3}
  .folder--navy .pocket-copy p,.folder--navy .pocket-copy h3{color:#e8ecf6}
  .folder--navy .pocket-copy .accent{color:var(--lime)}
  .folder--lime .pocket-copy p,.folder--lime .pocket-copy h3,.folder--lime .pocket-copy .accent{color:var(--navy)}
</style>
</head>
<body>

<!-- Option A: navy pocket -->
<section class="folder folder--navy">
  <svg class="dieline" viewBox="0 0 652 518" aria-hidden="true">
    <path d="M8,0 L644,0 L652,8 L652,186 A12,12 0 0 0 652,210 L652,368 L644,376 L626,376 L626,506 Q626,518 614,518 L36,518 Q24,518 24,506 L24,376 L8,376 L0,368 L0,210 A12,12 0 0 0 0,186 L0,8 Z" fill="none" stroke="var(--dieline)" stroke-width="0.8"/>
    <g stroke="var(--fold)" stroke-width="0.8" stroke-dasharray="2 2">
      <line x1="24" y1="0" x2="24" y2="376"/><line x1="626" y1="0" x2="626" y2="376"/>
      <line x1="325" y1="0" x2="325" y2="518"/><line x1="24" y1="376" x2="626" y2="376"/>
    </g>
  </svg>

  <div class="corner-wash" aria-hidden="true"></div>
  <div class="panel-frame cover-left"></div>
  <div class="photo photo--beach" role="img" aria-label="Photo of a multi-generation family walking hand in hand on a sunny beach"></div>
  <div class="ribbon ribbon--left" role="img" aria-label="Awareness ribbon in pink and blue"></div>
  <div class="cover-copy">
    <p><b>Hereditary cancer screening</b> provides vital information to help people with a strong personal or family history of cancer understand their own risk of developing the disease. With this information, they can take steps to Potentially Prevent Cancer, Delay the Onset of Cancer or Catch it at an Earlier stage when outcomes and survival rates are Better.</p>
    <p class="closing">Don't be Afraid of the Answer: Knowledge is Power and Power Eradicates Fear. When You are Fearless, You Will Make all the Right Choices!</p>
  </div>

  <div class="panel-frame cover-right"></div>
  <div class="title-band">HEREDITARY CANCER SCREENING</div>
  <p class="lead">Doctors are the Gatekeepers to Genetic Testing.</p>
  <p class="sublead">We have an obligation to help patients understand genetic risk and how testing can guide heath care decisions.</p>
  <div class="photo photo--table" role="img" aria-label="Photo of a family sharing a meal at an outdoor table"></div>
  <div class="ribbon ribbon--right" role="img" aria-label="Awareness ribbon in pink and blue"></div>
  <div class="tagline-band">The test you order FOR your patients</div>
  <div class="badge" aria-hidden="true"></div>

  <div class="pocket pocket--left">
    <div class="pocket-strip"></div>
    <div class="pocket-wash" aria-hidden="true"></div>
    <div class="flipped brand-block">
      <p class="brand-note">a division of Halden Medical Sales LLC</p>
      <p class="brand-name">Corvane Care Group</p>
    </div>
    <div class="flipped brand-mark"><div class="dot"></div><span>CORVANE CARE GROUP</span></div>
    <svg class="card-slits" viewBox="0 0 300 142" aria-hidden="true">
      <g stroke="var(--dieline)" stroke-width="0.8">
        <line x1="90" y1="66" x2="110" y2="50"/><line x1="90" y1="112" x2="110" y2="128"/>
        <line x1="232" y1="104" x2="212" y2="124"/><line x1="232" y1="42" x2="212" y2="26"/>
      </g>
    </svg>
  </div>

  <div class="pocket pocket--right">
    <div class="pocket-fill"></div>
    <div class="pocket-strip"></div>
    <div class="pocket-frame"></div>
    <div class="flipped pocket-copy">
      <p>Hereditary cancer screening provides vital information to help people with a strong personal or family history of cancer understand their own risk of developing the disease. With this information, they can take steps to Potentially Prevent Cancer, Delay the Onset of Cancer or Catch it at an Earlier stage when outcomes and survival rates are Better.</p>
      <h3>Identifying an inherited genetic mutation<br>has the potential to prevent cancer<br><span class="accent">and saves lives.</span></h3>
    </div>
  </div>
</section>

<!-- Option B: lime pocket -->
<section class="folder folder--lime">
  <svg class="dieline" viewBox="0 0 652 518" aria-hidden="true">
    <path d="M8,0 L644,0 L652,8 L652,186 A12,12 0 0 0 652,210 L652,368 L644,376 L626,376 L626,506 Q626,518 614,518 L36,518 Q24,518 24,506 L24,376 L8,376 L0,368 L0,210 A12,12 0 0 0 0,186 L0,8 Z" fill="none" stroke="var(--dieline)" stroke-width="0.8"/>
    <g stroke="var(--fold)" stroke-width="0.8" stroke-dasharray="2 2">
      <line x1="24" y1="0" x2="24" y2="376"/><line x1="626" y1="0" x2="626" y2="376"/>
      <line x1="325" y1="0" x2="325" y2="518"/><line x1="24" y1="376" x2="626" y2="376"/>
    </g>
  </svg>

  <div class="corner-wash" aria-hidden="true"></div>
  <div class="panel-frame cover-left"></div>
  <div class="photo photo--beach" role="img" aria-label="Photo of a multi-generation family walking hand in hand on a sunny beach"></div>
  <div class="ribbon ribbon--left" role="img" aria-label="Awareness ribbon in pink and blue"></div>
  <div class="cover-copy">
    <p><b>Hereditary cancer screening</b> provides vital information to help people with a strong personal or family history of cancer understand their own risk of developing the disease. With this information, they can take steps to Potentially Prevent Cancer, Delay the Onset of Cancer or Catch it at an Earlier stage when outcomes and survival rates are Better.</p>
    <p class="closing">Don't be Afraid of the Answer: Knowledge is Power and Power Eradicates Fear. When You are Fearless, You Will Make all the Right Choices!</p>
  </div>

  <div class="panel-frame cover-right"></div>
  <div class="title-band">HEREDITARY CANCER SCREENING</div>
  <p class="lead">Doctors are the Gatekeepers to Genetic Testing.</p>
  <p class="sublead">We have an obligation to help patients understand genetic risk and how testing can guide heath care decisions.</p>
  <div class="photo photo--table" role="img" aria-label="Photo of a family sharing a meal at an outdoor table"></div>
  <div class="ribbon ribbon--right" role="img" aria-label="Awareness ribbon in pink and blue"></div>
  <div class="tagline-band">The test you order FOR your patients</div>
  <div class="badge" aria-hidden="true"></div>

  <div class="pocket pocket--left">
    <div class="pocket-strip"></div>
    <div class="pocket-wash" aria-hidden="true"></div>
    <div class="flipped brand-block">
      <p class="brand-note">a division of Halden Medical Sales LLC</p>
      <p class="brand-name">Corvane Care Group</p>
    </div>
    <div class="flipped brand-mark"><div class="dot"></div><span>CORVANE CARE GROUP</span></div>
    <svg class="card-slits" viewBox="0 0 300 142" aria-hidden="true">
      <g stroke="var(--dieline)" stroke-width="0.8">
        <line x1="90" y1="66" x2="110" y2="50"/><line x1="90" y1="112" x2="110" y2="128"/>
        <line x1="232" y1="104" x2="212" y2="124"/><line x1="232" y1="42" x2="212" y2="26"/>
      </g>
    </svg>
  </div>

  <div class="pocket pocket--right">
    <div class="pocket-fill"></div>
    <div class="pocket-strip"></div>
    <div class="pocket-frame"></div>
    <div class="flipped pocket-copy">
      <p>Hereditary cancer screening provides vital information to help people with a strong personal or family history of cancer understand their own risk of developing the disease. With this information, they can take steps to Potentially Prevent Cancer, Delay the Onset of Cancer or Catch it at an Earlier stage when outcomes and survival rates are Better.</p>
      <h3>Identifying an inherited genetic mutation<br>has the potential to prevent cancer<br><span class="accent">and saves lives.</span></h3>
    </div>
  </div>
</section>

</body>
</html>
```